Legal Service Estimated Retainer and Average Case Value

We need an 11x14 flyer that contains the standard retainers and average cost be case, both provided in documents, for each case type we handle. We need the information displayed, preferably in a way that makes the information readable but less troubling to a client shocked at price of litigation. We need one sheet with the retainers and average case value merged into one table.

Target Market(s)

Potential Clients

Font styles to use
Serif
Sans Serif

```html
<!DOCTYPE html>
<html lang="en">
<head>
<meta charset="utf-8">
<title>Fee Guide – The Law Office of Mara T. Whitfield</title>
<link rel="stylesheet" href="https://fonts.googleapis.com/css2?family=Barlow+Semi+Condensed:wght@400;500;600&family=Libre+Baskerville&display=swap">
<style>
  :root {
    --backdrop: #5a5a5c;
    --paper: #ffffff;
    --navy: #3a3d55;
    --ink-navy: #1c2a55;
    --royal: #1b4aa0;
    --sky: #4a72c0;
    --band: #ececec;
    --table-bg: #f3f3f3;
    --rule: #8a8a8a;
    --text: #222;
  }
  * { box-sizing: border-box; margin: 0; padding: 0; }
  html, body { width: 1200px; height: 1200px; overflow: hidden; }
  body { background: var(--backdrop); position: relative; font-family: "Barlow Semi Condensed", sans-serif; color: var(--text); }

  .sheet { position: absolute; left: 213px; top: 130px; width: 772px; height: 990px; background: var(--paper); box-shadow: 0 4px 14px rgba(0,0,0,.35); overflow: hidden; }

  .brand { position: absolute; left: 58px; top: 28px; display: flex; align-items: center; gap: 12px; font-family: "Libre Baskerville", serif; color: var(--ink-navy); }
  .brand-mark { width: 46px; height: 46px; background: var(--ink-navy); }
  .brand-name { line-height: 1.05; }
  .brand-name small { display: block; font-size: 11px; letter-spacing: .5px; }
  .brand-name span { display: block; font-size: 22px; letter-spacing: .5px; }

  .contact { position: absolute; left: 453px; top: 35px; font-size: 13px; line-height: 16px; color: var(--text); }
  .contact strong { display: block; font-weight: 600; }
  .contact p { display: flex; align-items: center; gap: 4px; }
  .contact svg { width: 10px; height: 10px; fill: var(--royal); }

  .intro { position: absolute; left: 0; top: 122px; width: 772px; height: 88px; background: var(--band); border-left: 7px solid var(--royal); padding: 14px 0 0 74px; font-size: 14.5px; line-height: 18.5px; }

  .fees { position: absolute; left: 52px; top: 229px; width: 672px; }
  .fees-head { display: flex; gap: 3px; height: 37px; }
  .fees-head div { display: flex; align-items: center; justify-content: center; color: #fff; font-family: "Libre Baskerville", serif; font-size: 17px; letter-spacing: .3px; }
  .head-case { width: 308px; background: var(--navy); }
  .head-fee { width: 179px; background: var(--sky); }
  .head-retainer { width: 179px; background: var(--royal); }

  .fees-body { background: var(--table-bg); padding: 0 11px 0 22px; border-bottom: 5px solid var(--royal); height: 622px; }
  .row { display: flex; align-items: center; border-bottom: 1px solid var(--rule); font-size: 14.5px; font-weight: 500; height: 40.8px; }
  .row:last-child { border-bottom: none; }
  .row.tall { height: 60px; align-items: flex-start; padding-top: 13px; }
  .case { width: 290px; }
  .case::before { content: "•"; color: var(--royal); margin-right: 5px; }
  .fee { width: 180px; padding-left: 21px; }
  .retainer { width: 150px; text-align: center; padding-left: 20px; }
  .retainer em { display: block; font-style: normal; color: var(--royal); font-size: 12.5px; margin-top: 2px; }

  .site { position: absolute; left: 0; top: 920px; width: 356px; height: 37px; background: var(--navy); border-radius: 0 19px 19px 0; display: flex; align-items: center; padding-left: 56px; gap: 10px; color: #fff; font-family: "Libre Baskerville", serif; font-size: 15.5px; }
  .site svg { width: 15px; height: 15px; }
  .social { position: absolute; left: 555px; top: 920px; width: 230px; height: 37px; border: 1.5px solid var(--navy); border-right: none; border-radius: 19px 0 0 19px; display: flex; align-items: center; gap: 13px; padding-left: 36px; }
  .social span { width: 24px; height: 24px; border-radius: 50%; background: var(--royal); }

  .foot-band { position: absolute; left: 0; bottom: 0; width: 772px; height: 10px; background: var(--ink-navy); }
</style>
</head>
<body>
  <main class="sheet">
    <header>
      <div class="brand">
        <div class="brand-mark"></div>
        <div class="brand-name"><small>THE LAW OFFICE OF</small><span>MARA T WHITFIELD</span></div>
      </div>
      <address class="contact" style="font-style:normal">
        <strong>The Law Office of Mara T. Whitfield</strong>
        <p><svg viewBox="0 0 10 10"><path d="M5 0a3.5 3.5 0 0 0-3.5 3.5C1.5 6 5 10 5 10s3.5-4 3.5-6.5A3.5 3.5 0 0 0 5 0zm0 5a1.5 1.5 0 1 1 0-3 1.5 1.5 0 0 1 0 3z"/></svg>2150 Orchard Hill Road, Suite 210, Riverton, PA 17045</p>
        <p><svg viewBox="0 0 10 10"><path d="M2 0.5l2 2-1 1.2c.6 1.3 1.6 2.3 2.9 2.9L7.1 5.6l2 2L8 9.5C4 9 1 6 .5 2z"/></svg>(555) 014-2288</p>
      </address>
    </header>

    <section class="intro">
      <p>In order for our clients to set expectations for legal fees, we provide the national average range of fees per case type.</p>
      <p>These are only to provide you with an understanding of what other cases have cost clients in similar cases.</p>
      <p>Please note these are not estimates nor guarantees of your own legal costs.</p>
    </section>

    <section class="fees">
      <div class="fees-head">
        <div class="head-case">CASE TYPES</div>
        <div class="head-fee">AVERAGE FEE</div>
        <div class="head-retainer">RETAINERS</div>
      </div>
      <div class="fees-body">
        <div class="row"><div class="case">Custody Contempt/Modification</div><div class="fee">$5,000 - $8,000</div><div class="retainer">$3,500</div></div>
        <div class="row"><div class="case">Custody Initial Order</div><div class="fee">$4,000 - $7,000</div><div class="retainer">$3,000</div></div>
        <div class="row"><div class="case">Custody &amp; Support</div><div class="fee">$5,000 - $8,000</div><div class="retainer">$3,000</div></div>
        <div class="row"><div class="case">Support</div><div class="fee">$2,000 - $4,000</div><div class="retainer"></div></div>
        <div class="row"><div class="case">Divorce (3301c)</div><div class="fee">$1,500 - $3,000</div><div class="retainer">$2,000</div></div>
        <div class="row"><div class="case">Divorce (3301d)</div><div class="fee">$2,000 - $3,000</div><div class="retainer">$2,500</div></div>
        <div class="row tall"><div class="case">Protection from Abuse (PFA)</div><div class="fee">$1,500 - $3,000</div><div class="retainer">$2,000<em>Paid In Full</em></div></div>
        <div class="row"><div class="case">Divorce &amp; Support</div><div class="fee"></div><div class="retainer">$3,000</div></div>
        <div class="row"><div class="case">Divorce &amp; Custody</div><div class="fee">$5,000 - $8,000</div><div class="retainer">$3,500</div></div>
        <div class="row"><div class="case">Divorce &amp; Equitable Distribution</div><div class="fee">$6,000 - $10,000</div><div class="retainer">$3,500</div></div>
        <div class="row"><div class="case">Divorce, Custody &amp; Support</div><div class="fee">$8,000 - $12,000</div><div class="retainer">$3,500</div></div>
        <div class="row"><div class="case">Divorce, Equitable Distribution &amp; Custody</div><div class="fee">$10,000 - $15,000</div><div class="retainer">$5,000</div></div>
        <div class="row"><div class="case">Divorce, Equitable Distribution &amp; Support</div><div class="fee">$8,000 - $12,000</div><div class="retainer">$3,500</div></div>
        <div class="row"><div class="case">Divorce, Equitable Distribution, Custody &amp; Support</div><div class="fee">$12,000 - $15,000</div><div class="retainer">$3,500</div></div>
      </div>
    </section>

    <footer>
      <div class="site">
        <svg viewBox="0 0 16 16" fill="none" stroke="#fff" stroke-width="1.3"><circle cx="8" cy="8" r="7"/><ellipse cx="8" cy="8" rx="3" ry="7"/><path d="M1 8h14M2.5 4.5h11M2.5 11.5h11"/></svg>
        www.whitfieldlawoffice.com
      </div>
      <div class="social" aria-label="Social media links"><span></span><span></span><span></span><span></span></div>
      <div class="foot-band"></div>
    </footer>
  </main>
</body>
</html>
```